Vemb - Website Design in WordPress (2 pages)

The goal of this design work is to create two highly focused, PPC- and SEO-aware landing pages that clearly explain the experience in familiar terms and drive app installs. The design must respect the existing visual identity and support future iteration of copy and content without requiring redesign.
Required Deliverables:
Fully working WordPress site containing:
Homepage template
Location landing page template
Mobile-first, responsive
CTA behaviour exactly as designed
Required
WordPress admin access
Full site export / backup
Homepage template
Mobile-first behaviour
CTA visible above the fold on mobile
Uses my:
Visual identity
Logo
Placeholder copy
I receive:
Admin access
Full site export / backup
Not acceptable
20+ plugins
Proprietary or abandoned builders
Hardcoded layouts that can’t be reused
Separate page designs per location
Elementor is preferred if:
One builder only
Clean structure
No custom lock-in widgets
Uploaded the mobile design for inspiration only
Coding
Coded - Design and coding required
Look and feel
Each slider illustrates characteristics of the customer's brand and the style your logo design should communicate.

```html
<!DOCTYPE html>
<html lang="en">
<head>
<meta charset="utf-8">
<title>Vemb – Walk, Solve Clues, and Play Together</title>
<link rel="stylesheet" href="https://fonts.googleapis.com/css2?family=League+Spartan:wght@600;700&family=Ubuntu:wght@400;500;700&family=Lato:wght@400&display=swap">
<style>
:root{
  --teal:#2aa9b5;
  --teal-deep:#157d8c;
  --teal-dark:#136f80;
  --teal-bright:#3bbfc9;
  --orange:#f05a28;
  --ink:#111418;
  --body:#5b6166;
  --grey-band:#e6e7e9;
  --white:#ffffff;
}
*{margin:0;padding:0;box-sizing:border-box}
html,body{width:1200px;height:2448px;overflow:hidden;background:var(--white)}
body{position:relative;font-family:'Lato',sans-serif;color:var(--body)}
.heading{font-family:'League Spartan',sans-serif;font-weight:700;color:var(--ink);letter-spacing:-0.5px}
.accent{color:var(--teal-deep)}
.rule{display:block;width:57px;height:4px;background:var(--teal-bright)}
.btn{position:absolute;z-index:2;display:flex;align-items:center;justify-content:center;background:var(--orange);color:var(--white);font-family:'League Spartan',sans-serif;font-weight:700;text-transform:uppercase;border-radius:0 24px 24px 24px;text-decoration:none}

/* hero */
.hero{position:absolute;left:0;top:0;width:1200px;height:598px;background:linear-gradient(120deg,#38b4bf 0%,#2aa4b0 45%,#1a8592 100%);border-bottom-right-radius:260px;overflow:hidden}
.hero__brand{position:absolute;z-index:2;left:145px;top:18px;font-family:'League Spartan',sans-serif;font-weight:700;font-size:54px;color:var(--white);letter-spacing:-1px}
.hero__cta-top{left:919px;top:25px;width:135px;height:40px;font-size:14px;border-radius:0 20px 20px 20px}
.hero__title{position:absolute;z-index:2;left:145px;top:165px;font-size:58px;line-height:64px;color:var(--white)}
.hero__cta{left:145px;top:400px;width:320px;height:48px;font-size:16px}
.hero__photo{position:absolute;z-index:1;left:625px;top:70px;width:500px;height:528px;border-radius:250px 250px 0 0;background:radial-gradient(ellipse at 50% 40%,#3f7a86 0%,#2b6470 55%,#236270 100%)}

/* steps */
.how{position:absolute;left:0;top:668px;width:1200px;text-align:center}
.how .heading{font-size:42px}
.how .rule{margin:12px auto 0}
.how__lead{margin-top:30px;font-size:14.5px}
.steps{position:absolute;left:140px;top:810px;width:920px;height:200px}
.step{position:absolute;top:0;width:240px;height:200px}
.step svg{position:absolute;left:0;top:0}
.step__num{position:absolute;left:0;width:196px;top:92px;text-align:center;font-family:'Ubuntu',sans-serif;font-weight:700;font-size:36px;color:var(--teal-bright)}
.step__label{position:absolute;left:0;width:196px;top:136px;text-align:center;font-family:'Ubuntu',sans-serif;font-weight:500;font-size:16px;line-height:24px;color:var(--ink)}

/* benefits */
.benefits{position:absolute;left:0;top:1076px;width:1200px;height:496px;background:radial-gradient(ellipse at 85% 30%,#1a7b8c 0%,var(--teal-dark) 60%);border-top-left-radius:220px}
.benefits .heading{position:absolute;left:0;width:1200px;top:62px;text-align:center;font-size:42px;color:var(--white)}
.benefits .rule{position:absolute;left:572px;top:127px}
.card{position:absolute;top:174px;width:296px;height:255px;background:var(--white);border-radius:18px;text-align:center}
.card svg{position:absolute;left:103px;top:28px}
.card__title{position:absolute;left:0;width:100%;top:149px;font-family:'Ubuntu',sans-serif;font-weight:400;font-size:18px;color:var(--ink);text-transform:uppercase}
.card__text{position:absolute;left:28px;width:240px;top:186px;font-size:14px;line-height:24px}

/* difference */
.diff__photo{position:absolute;left:136px;top:1650px;width:416px;height:414px;border-radius:208px 208px 208px 0;background:var(--teal-bright)}
.diff__photo-fill{position:absolute;left:8px;top:0;width:408px;height:406px;border-radius:204px 204px 204px 0;background:linear-gradient(135deg,#8a7566 0%,#5a4a44 40%,#3b3436 70%,#6b6a70 100%)}
.diff{position:absolute;left:615px;top:1662px;width:440px}
.diff .heading{font-size:42px;white-space:nowrap}
.diff .rule{margin-top:16px}
.diff__list{list-style:none;margin-top:40px}
.diff__item{margin-bottom:20px}
.diff__item h3{font-family:'Ubuntu',sans-serif;font-weight:400;font-size:18px;color:var(--ink);display:flex;align-items:center;gap:9px}
.diff__item p{margin:12px 0 0 22px;font-size:14px;line-height:23px;text-align:justify}

/* capture */
.capture{position:absolute;left:0;top:2131px;width:1200px;height:317px;background:var(--grey-band);border-top-right-radius:260px}
.capture .heading{position:absolute;left:0;width:1200px;top:56px;text-align:center;font-size:44px}
.capture__text{position:absolute;left:160px;width:880px;top:126px;text-align:center;font-size:14px;line-height:24px}
.capture__cta{left:448px;top:202px;width:304px;height:44px;font-size:16px}
.footer{position:absolute;left:144px;top:271px;width:912px;border-top:1px solid #c9cbce;padding-top:14px;text-align:center;font-size:13px;color:var(--ink)}
</style>
</head>
<body>

<header class="hero">
  <div class="hero__photo" role="img" aria-label="Photo of an excited young man holding a smartphone and raising his hand"></div>
  <div class="hero__brand">Vemb</div>
  <a class="btn hero__cta-top" href="#">Get the app</a>
  <h1 class="heading hero__title">Walk, Solve Clues,<br>and Play Together<br>Using The App</h1>
  <a class="btn hero__cta" href="#">Download on the App Shelf</a>
</header>

<section class="how">
  <h2 class="heading"><span class="accent">How</span> It Works</h2>
  <span class="rule"></span>
  <p class="how__lead">Lorem ipsum dolor sit amet, consectetur adipiscing elit, sed do eiusmod tempor incididunt</p>
</section>

<div class="steps">
  <div class="step" style="left:0">
    <svg width="240" height="200" viewBox="0 0 240 200">
      <path d="M14 190 A90 90 0 1 1 182 190" fill="none" stroke="var(--teal-deep)" stroke-width="18"/>
      <path d="M196 122 L222 122 L230 134 L222 146 L196 146 Z" fill="var(--teal-deep)"/>
      <circle cx="98" cy="43" r="45" fill="var(--teal-bright)"/>
      <g fill="none" stroke="#fff" stroke-width="2.2">
        <rect x="82" y="22" width="32" height="40" rx="4"/>
        <path d="M98 30v20M90 43l8 8 8-8M90 56h16"/>
      </g>
    </svg>
    <div class="step__num">01</div>
    <div class="step__label">Download the<br>app</div>
  </div>
  <div class="step" style="left:244px">
    <svg width="240" height="200" viewBox="0 0 240 200">
      <path d="M14 190 A90 90 0 1 1 182 190" fill="none" stroke="var(--teal-deep)" stroke-width="18"/>
      <path d="M196 122 L222 122 L230 134 L222 146 L196 146 Z" fill="var(--teal-deep)"/>
      <circle cx="98" cy="43" r="45" fill="var(--teal-bright)"/>
      <g fill="none" stroke="#fff" stroke-width="2.2">
        <circle cx="98" cy="52" r="13"/><path d="M92 52l4 4 8-8"/>
        <path d="M98 18l3 7 7 1-5 5 1 7-6-3-6 3 1-7-5-5 7-1z"/>
        <path d="M76 34l2 5 5 1-4 3 1 5-4-2-4 2 1-5-4-3 5-1z"/>
        <path d="M120 34l2 5 5 1-4 3 1 5-4-2-4 2 1-5-4-3 5-1z"/>
      </g>
    </svg>
    <div class="step__num">01</div>
    <div class="step__label">Choose an<br>experience</div>
  </div>
  <div class="step" style="left:488px">
    <svg width="240" height="200" viewBox="0 0 240 200">
      <path d="M14 190 A90 90 0 1 1 182 190" fill="none" stroke="var(--teal-deep)" stroke-width="18"/>
      <path d="M196 122 L222 122 L230 134 L222 146 L196 146 Z" fill="var(--teal-deep)"/>
      <circle cx="98" cy="43" r="45" fill="var(--teal-bright)"/>
      <g fill="none" stroke="#fff" stroke-width="2.2">
        <path d="M98 16l24 14v26l-24 14-24-14V30z"/>
        <circle cx="98" cy="38" r="5"/><circle cx="86" cy="44" r="4"/><circle cx="110" cy="44" r="4"/>
        <path d="M88 58c0-7 20-7 20 0M80 55c0-5 10-5 10-2M116 55c0-5-10-5-10-2"/>
      </g>
    </svg>
    <div class="step__num">01</div>
    <div class="step__label">Meet your group<br>and start</div>
  </div>
  <div class="step" style="left:720px">
    <svg width="240" height="200" viewBox="0 0 240 200">
      <path d="M14 190 A90 90 0 1 1 182 190" fill="none" stroke="var(--teal-deep)" stroke-width="18"/>
      <circle cx="98" cy="43" r="45" fill="var(--teal-bright)"/>
      <g fill="none" stroke="#fff" stroke-width="2.2">
        <path d="M84 22h28v14a14 14 0 0 1-28 0z"/>
        <path d="M84 26h-8a8 8 0 0 0 8 12M112 26h8a8 8 0 0 1-8 12"/>
        <path d="M98 50v8M88 64h20M92 58h12"/>
        <path d="M98 26l2 4 4 1-3 3 1 4-4-2-4 2 1-4-3-3 4-1z"/>
      </g>
    </svg>
    <div class="step__num">01</div>
    <div class="step__label">Complete the<br>experience</div>
  </div>
</div>

<section class="benefits">
  <h2 class="heading">App Benefits</h2>
  <span class="rule"></span>

  <article class="card" style="left:144px">
    <svg width="90" height="90" viewBox="0 0 90 90" fill="none" stroke="var(--teal-deep)" stroke-width="3">
      <path d="M45 4l6 8 10-2 2 10 9 5-4 9"/><path d="M45 4l-6 8-10-2-2 10-9 5 4 9"/>
      <circle cx="45" cy="34" r="8"/><circle cx="25" cy="46" r="6"/><circle cx="65" cy="46" r="6"/>
      <path d="M31 86V62c0-14 28-14 28 0v24M11 86V68c0-10 18-10 18 0M79 86V68c0-10-18-10-18 0"/>
      <path d="M8 86h74"/>
    </svg>
    <h3 class="card__title">What users do</h3>
    <p class="card__text">Lorem ipsum dolor amet, consectetur adipiscing elit, sed do eiusmod</p>
  </article>

  <article class="card" style="left:452px">
    <svg width="90" height="90" viewBox="0 0 90 90" fill="none" stroke="var(--teal-deep)" stroke-width="3">
      <rect x="22" y="4" width="46" height="82" rx="6"/><path d="M38 80h14"/>
      <rect x="52" y="8" width="26" height="22" rx="4"/><path d="M65 24l-6-6a3 3 0 0 1 6-3 3 3 0 0 1 6 3z"/>
      <rect x="10" y="38" width="24" height="22" rx="4"/><path d="M22 42l2 5 5 1-4 3 1 5-4-3-4 3 1-5-4-3 5-1z"/>
      <rect x="28" y="20" width="22" height="18" rx="3"/><circle cx="66" cy="66" r="8"/>
      <path d="M36 64h2M44 64h2M52 64h2"/>
    </svg>
    <h3 class="card__title">Social aspect</h3>
    <p class="card__text">Lorem ipsum dolor amet, consectetur adipiscing elit, sed do eiusmod</p>
  </article>

  <article class="card" style="left:760px">
    <svg width="90" height="90" viewBox="0 0 90 90" fill="none" stroke="var(--teal-deep)" stroke-width="3">
      <path d="M6 10h40v76H6z"/><path d="M6 10l34-6v82"/><path d="M46 10h10v18M56 62v24H46"/>
      <path d="M30 46a4 4 0 0 1 0 8"/>
      <path d="M56 38h12v-10l18 17-18 17v-10H56z" fill="var(--teal-bright)"/>
    </svg>
    <h3 class="card__title">Outdoor aspect</h3>
    <p class="card__text">Lorem ipsum dolor amet, consectetur adipiscing elit, sed do eiusmod</p>
  </article>
</section>

<div class="diff__photo">
  <div class="diff__photo-fill" role="img" aria-label="Photo of a group of smiling friends gathered together looking at their phones"></div>
</div>

<section class="diff">
  <h2 class="heading"><span class="accent">What</span> Makes It Different</h2>
  <span class="rule"></span>
  <ul class="diff__list">
    <li class="diff__item">
      <h3><svg width="12" height="12" viewBox="0 0 12 12"><circle cx="6" cy="6" r="6" fill="var(--teal-bright)"/><path d="M3 6l2 2 4-4" stroke="#fff" stroke-width="1.6" fill="none"/></svg>Difference vs escape rooms</h3>
      <p>Lorem ipsum dolor sit amet, consectetur adipiscing elit, sed do eiusmod tempor incididunt ut labore et dolore</p>
    </li>
    <li class="diff__item">
      <h3><svg width="12" height="12" viewBox="0 0 12 12"><circle cx="6" cy="6" r="6" fill="var(--teal-bright)"/><path d="M3 6l2 2 4-4" stroke="#fff" stroke-width="1.6" fill="none"/></svg>Difference vs treasure hunts</h3>
      <p>Lorem ipsum dolor sit amet, consectetur adipiscing elit, sed do eiusmod tempor incididunt ut labore et dolore</p>
    </li>
    <li class="diff__item">
      <h3><svg width="12" height="12" viewBox="0 0 12 12"><circle cx="6" cy="6" r="6" fill="var(--teal-bright)"/><path d="M3 6l2 2 4-4" stroke="#fff" stroke-width="1.6" fill="none"/></svg>Difference vs casual walks</h3>
      <p>Lorem ipsum dolor sit amet, consectetur adipiscing elit, sed do eiusmod tempor incididunt ut labore et dolore</p>
    </li>
  </ul>
</section>

<section class="capture">
  <h2 class="heading"><span class="accent">Capture</span> Users Who <span class="accent">Scrolled</span> For Confirmation</h2>
  <p class="capture__text">Lorem ipsum dolor sit amet, consectetur adipiscing elit, sed do eiusmod tempor incididunt ut labore et dolore magna aliqua. Ut enim ad minim veniam, quis nostrud exercitation ullamco laboris nisi ut aliquip ex ea commodo consequat.</p>
  <a class="btn capture__cta" href="#">Download on the App Shelf</a>
  <footer class="footer">Copyright© 2026 Vemb &nbsp;|&nbsp; All Rights Reserved</footer>
</section>

</body>
</html>
```